Coffee Bag Label

I need a coffee bag label designed (front label and back label):
Our company "Tidy-Pod" imports organic coffee beans direct from a farm on Osoruto Mountain on a private reserve (rainforest) from Jinotega, Nicaragua.
Labels should each be 3 inches x 3 inches (with room on edges for bleed). I want the front label to catch the eye and coordinate well with the coffee bag. The bags sizes are below and pictures are attached.
Bag sizes: Lime green 12 oz bag: 3-3/8" x 2-9/16" x 10-1/4"
Black 2 oz sample stand up pouch: 4" x 6-1/2" + 2-3/8", 2oz (60g)
Black 2lb bag: 5" x 3-3/8" x 15", 2lb (1kg)
Please include as much as possible below on the front label without it looking too wordy:
1) Our logo (it's attached). Feel free to do something creative with just the bean and place "Tidy-Pod" or "Tidy-Pod Coffees" somewhere else. They don't have to be together like in the attached file. The bean can be in the background of the label as well or something else cool like in the form of a cloud over the volcano or as the sun in the sky over the volcano.
2) lime green, burnt orange, dark brown & black
3) Front label should say:
"100% Premium Arabica Nicaraguan Coffee"
"Organic, Rain Forest & Mountain Shade Grown"
Bottom of label:
"Medium Roast"
"Full body, bold flavor, nutty, hints of chocolate, with a distinct & flavorful aroma."
I want one front label file for each size bag: "2 oz" "12 oz" & "32 oz"
Back of the label:
I have uploaded a hand drawn pic of what I am thinking but if you have a better idea please submit it.
Please include as much as possible below without it looking wordy:
Directions on the perfect cup:
***2 Tbsp high quality coffee 6 Oz. cup of pure filtered water
(these can be tied into the hand-drawn picture. I will label the section each one corresponds to)
Organically Grown (sustainable)
Rainforest Grown (sustainable)
Mountain Shade Grown (sustainable)
Hand Picked (select)
Spring Water Washed (select)
Sun Dried (select)
Social Responsibility (profits help fund Bright Path Outreach Nicaragua www.brightpathoutreach.org)
Single Source Coffee (Single source)
Traceable Source (single source)
Website: www.Tidy-Pod.com
Updates
Project Deadline Extended
Reason: I have been asked to extend deadline by a few designers.
Thanks,
Danita Crowe
Target Market(s)
ages 18-54
Requirements
Must have
- Should have a cool border. Maybe fade from one color to another or have something more original than just a 3x3 square border.

```html
<!DOCTYPE html>
<html lang="en">
<head>
<meta charset="utf-8">
<title>Tidy-Pod Medium Roast Label</title>
<link rel="stylesheet" href="https://fonts.googleapis.com/css2?family=Josefin+Sans:wght@400;600&family=Pinyon+Script&family=Arimo:wght@700&family=Tinos:ital@1&display=swap">
<style>
  :root {
    --ink-black: #000000;
    --lime: #7cc242;
    --rim-brown: #5a2e14;
    --bean-brown: #4a2412;
    --gold-hot: #ffe36a;
    --gold: #f2b62a;
    --burnt-orange: #c86a1c;
    --edge-brown: #7a3e16;
    --roast-red: #9a1a12;
    --band-dark: #2a1208;
    --copy-orange: #f07a22;
    --copy-italic: #e8742a;
    --parchment-light: #f3e2b8;
    --parchment-dark: #c9a86a;
  }
  html, body {
    margin: 0;
    width: 1200px;
    height: 1000px;
    overflow: hidden;
    background: var(--ink-black);
  }
  .label-canvas { display: block; width: 1200px; height: 1000px; }
  .brand-name {
    font-family: "Josefin Sans", sans-serif;
    font-weight: 600;
    font-size: 104px;
    fill: var(--bean-brown);
  }
  .brand-sub {
    font-family: "Josefin Sans", sans-serif;
    font-weight: 600;
    font-size: 24px;
    letter-spacing: 2px;
    fill: var(--bean-brown);
  }
  .roast-title {
    font-family: "Pinyon Script", cursive;
    font-size: 76px;
    fill: var(--roast-red);
  }
  .origin-line {
    font-family: "Arimo", sans-serif;
    font-weight: 700;
    font-size: 21px;
    fill: var(--copy-orange);
  }
  .tasting-note {
    font-family: "Tinos", serif;
    font-style: italic;
    font-size: 24px;
    fill: var(--copy-italic);
  }
  .net-weight {
    font-family: "Arimo", sans-serif;
    font-weight: 700;
    font-size: 32px;
    fill: var(--lime);
  }
</style>
</head>
<body>
<svg class="label-canvas" viewBox="0 0 1200 1000" xmlns="http://www.w3.org/2000/svg">
  <defs>
    <path id="label-outline" d="M255,150 L330,150 Q352,150 362,122 Q386,65 442,65 L758,65 Q814,65 838,122 Q848,150 870,150 L935,150 Q985,150 985,200 L985,870 Q985,920 935,920 L255,920 Q205,920 205,870 L205,200 Q205,150 255,150 Z"/>
    <clipPath id="label-clip"><use href="#label-outline"/></clipPath>
    <radialGradient id="sunburst" cx="600" cy="330" r="480" gradientUnits="userSpaceOnUse">
      <stop offset="0" stop-color="var(--gold-hot)"/>
      <stop offset="0.35" stop-color="var(--gold)"/>
      <stop offset="0.7" stop-color="var(--burnt-orange)"/>
      <stop offset="1" stop-color="var(--edge-brown)"/>
    </radialGradient>
    <linearGradient id="band-fade" x1="0" y1="0" x2="0" y2="1">
      <stop offset="0" stop-color="#4a1e0c"/>
      <stop offset="1" stop-color="var(--band-dark)"/>
    </linearGradient>
    <linearGradient id="scroll-paper" x1="0" y1="0" x2="0" y2="1">
      <stop offset="0" stop-color="var(--parchment-light)"/>
      <stop offset="1" stop-color="var(--parchment-dark)"/>
    </linearGradient>
    <linearGradient id="scroll-roll" x1="0" y1="0" x2="1" y2="0">
      <stop offset="0" stop-color="var(--parchment-dark)"/>
      <stop offset="0.5" stop-color="var(--parchment-light)"/>
      <stop offset="1" stop-color="var(--parchment-dark)"/>
    </linearGradient>
    <linearGradient id="landscape-tones" x1="0" y1="0" x2="0" y2="1">
      <stop offset="0" stop-color="#2f6fc4"/>
      <stop offset="0.35" stop-color="#a9c9ec"/>
      <stop offset="0.55" stop-color="#5d8a8f"/>
      <stop offset="0.75" stop-color="#2f6a2a"/>
      <stop offset="1" stop-color="#1e4a1c"/>
    </linearGradient>
  </defs>

  <!-- outer lime rim -->
  <use href="#label-outline" fill="none" stroke="var(--lime)" stroke-width="14"/>
  <!-- label field -->
  <use href="#label-outline" fill="url(#sunburst)"/>

  <g clip-path="url(#label-clip)">
    <!-- lower copy band -->
    <rect class="copy-band" x="200" y="732" width="800" height="200" fill="url(#band-fade)"/>
    <!-- inner rim -->
    <use href="#label-outline" fill="none" stroke="var(--lime)" stroke-width="38"/>
    <use href="#label-outline" fill="none" stroke="var(--rim-brown)" stroke-width="30"/>
  </g>

  <!-- brand -->
  <circle class="brand-dot" cx="600" cy="150" r="44" fill="var(--bean-brown)"/>
  <text class="brand-name" x="600" y="318" text-anchor="middle">Tidy-Pod</text>
  <text class="brand-sub" x="600" y="354" text-anchor="middle">ORGANIC COFFEE</text>
  <text class="roast-title" x="604" y="424" text-anchor="middle">Medium Roast</text>

  <!-- scroll frame -->
  <g class="scroll-frame">
    <rect x="280" y="456" width="620" height="252" fill="url(#scroll-paper)"/>
    <rect x="266" y="448" width="28" height="268" rx="8" fill="url(#scroll-roll)"/>
    <rect x="886" y="448" width="28" height="268" rx="8" fill="url(#scroll-roll)"/>
    <rect x="316" y="470" width="546" height="222" fill="#ffffff"/>
    <rect class="landscape" x="322" y="476" width="534" height="210" fill="url(#landscape-tones)" role="img" aria-label="Photo of a forested green volcano under a blue sky with clouds"/>
  </g>

  <!-- copy -->
  <text class="origin-line" x="596" y="759" text-anchor="middle">100% Premium Arabica Nicaraguan Coffee</text>
  <text class="origin-line" x="596" y="793" text-anchor="middle">Organic, Rain Forest &amp; Mountain Shade Grown</text>
  <text class="tasting-note" x="596" y="832" text-anchor="middle">Full body, bold flavor, nutty, hints of chocolate, with a</text>
  <text class="tasting-note" x="596" y="866" text-anchor="middle">distinct &amp; flavorful aroma.</text>
  <text class="net-weight" x="294" y="876">2oz</text>

  <!-- certification badge -->
  <ellipse class="cert-badge" cx="862" cy="866" rx="34" ry="18" fill="#ffffff" stroke="var(--lime)" stroke-width="4"/>
</svg>
</body>
</html>
```